TKL Accounting Firm Needs Graphic Art for Our Proven Processes and For Our Core Values

**Looking for redesign of attached Powerpoint content (see below)
***Final graphic should be good for web use

Date: March 10, 2017

From: Curtis Alvarado, CPA
Tolbert, Kinsley & Associates, P.C. (TKL)

Background:

TKL is a 20 person Houston based CPA firm, providing tax, accounting, financial and consulting services, to individuals and to entrepreneurs and their businesses. TKL is engaged in a process called BTF (See the book Momentum, by Lars Pendleton) whereby we implement a “system” to operate our company. As part of this system we have defined what we call our “Proven Process”. This is something we will show all prospective clients, and have on our website, that explains what it looks like to work with us. Starting at the beginning of the project to completion.

Project Description:

TKL is looking for graphic artist assistance in designing the following pieces:

1. Graphic depiction of “The TKL Way”, otherwise known as our “Proven Process”. The first attachments labeled TKL will show what we have done ourselves. These will show the general steps we have defined in both a sort of graphic way and a step by step narrative. The second attachment shows you some actual examples other firms have put together, hopefully that will show you what we are asking you to develop for us. Note that we are very open to any suggested clarifications or improvements to what we have done which may include changing phrases or saying something in a different way. Remember we are accountants!

2. We have defined our core values as a company, and we are wanting to develop some posters/placards so we can post them in our conference rooms, break room, etc. Attached are our core values as well as some deeper narratives about what they mean. Also included are many of the “words” we kicked around before arriving at our core values.

3. You will also find an attachment with our logo that should be incorporated, as well. Designs SHOULD INCLUDE, but not be limited to, the colors on our logo. Our end product should reflect a strong sense of our core values.

We would like to have the project in a form that would give us the option to use any/all of the information on our website, posters, brochures, etc.

Thanks in advance for your assistance.

Project Deadline Extended Reason: We are in the midst of tax deadlines so need a little more time to review and respond. Added Monday, March 20, 2017

Target Market(s)

Entrepreneurs and their companies with revenue greater than one million; Industries such as real estate, construction, trades and professional services; all in the Greater Houston Texas area

Industry/Entity Type

Accounting

Font styles to use
Serif
Other font styles liked:
• We are okay with Serif but are open.

Requirements
Must have
• Proven Process must be presented in a way that is clear and makes sense.
Nice to have
• Clean lines
• Colors should go with logo (see attached)
Should not have
• Can't think of anything - unless I see it

```html
<!DOCTYPE html>
<html lang="en">
<head>
<meta charset="utf-8">
<title>Client Service Approach – Tolbert, Kinsley &amp; Associates, P.C.</title>
<link rel="stylesheet" href="https://fonts.googleapis.com/css2?family=Open+Sans:wght@400;700;800&display=swap">
<style>
  :root {
    --bg: #ffffff;
    --title: #555555;
    --brand: #3f3f3f;
    --brand-mark: #a0832e;
    --footer-rule: #c9c9c9;
    --footer-end: #e2e2e2;
    --peace: #e72f7b;
    --caring: #238fd2;
    --focus: #f7dc2e;
    --navy: #1f1a66;
    --red: #d7261f;
    --green: #287d2b;
    --core: #221816;
    --label: #ffffff;
  }
  * { margin: 0; padding: 0; box-sizing: border-box; }
  html, body { width: 1200px; height: 675px; overflow: hidden; background: var(--bg); }
  .slide {
    position: relative;
    width: 1200px;
    height: 675px;
    overflow: hidden;
    background: var(--bg);
    font-family: "Open Sans", Arial, sans-serif;
  }
  .slide-title {
    position: absolute;
    left: 30px;
    top: 36px;
    font-weight: 700;
    font-size: 45px;
    letter-spacing: 0.3px;
    color: var(--title);
    line-height: 1;
  }
  .approach-diagram {
    position: absolute;
    left: 0;
    top: 0;
    width: 1200px;
    height: 675px;
  }
  .approach-label {
    font-family: "Open Sans", Arial, sans-serif;
    font-weight: 800;
    font-size: 31px;
    fill: var(--label);
    letter-spacing: -0.3px;
  }
  .slide-footer {
    position: absolute;
    left: 0;
    right: 0;
    bottom: 0;
    height: 112px;
    border-top: 2px solid var(--footer-rule);
    background: linear-gradient(90deg, var(--bg) 0%, var(--bg) 35%, var(--footer-end) 100%);
  }
  .firm-brand {
    position: absolute;
    left: 30px;
    top: 22px;
    width: 320px;
    display: flex;
    flex-direction: column;
    align-items: center;
    gap: 12px;
  }
  .firm-brand-square {
    width: 30px;
    height: 30px;
    background: var(--brand-mark);
  }
  .firm-brand-name {
    font-weight: 400;
    font-size: 19px;
    color: var(--brand);
    white-space: nowrap;
  }
</style>
</head>
<body>
  <main class="slide">
    <h1 class="slide-title">CLIENT SERVICE APPROACH</h1>

    <svg class="approach-diagram" viewBox="0 0 1200 675" aria-labelledby="approach-title">
      <title id="approach-title">Client service approach: peace of mind, caring touch and client focus</title>
      <g class="approach-hexagon">
        <polygon class="segment-peace" fill="var(--peace)" points="471,127 625,127 472,394 395,261"/>
        <polygon class="segment-caring" fill="var(--caring)" points="625,127 782,127 858,261 780,394"/>
        <polygon class="segment-focus" fill="var(--focus)" points="472,394 780,394 704,527 547,527"/>
        <polygon class="segment-top" fill="var(--navy)" points="625,127 550,261 702,261"/>
        <polygon class="segment-left" fill="var(--red)" points="550,261 472,394 625,394"/>
        <polygon class="segment-right" fill="var(--green)" points="702,261 625,394 780,394"/>
        <polygon class="segment-core" fill="var(--core)" points="550,261 702,261 625,394"/>
      </g>

      <text class="approach-label" text-anchor="middle" transform="translate(540 257) rotate(-60)">Peace of mind</text>
      <text class="approach-label" text-anchor="middle" transform="translate(716 252) rotate(60)">Caring touch</text>
      <text class="approach-label" text-anchor="middle" x="621" y="421">Client focus</text>
    </svg>

    <footer class="slide-footer">
      <div class="firm-brand">
        <span class="firm-brand-square"></span>
        <span class="firm-brand-name">Tolbert, Kinsley &amp; Associates, P.C.</span>
      </div>
    </footer>
  </main>
</body>
</html>
```